Harborlight Energy Local Letter Drop

I need a compelling and visually appealing flyer to promote our solar installation company in our local area of Boronia Victoria.
Because we are an install company without the overheads of the big solar sales companies, we pride ourselves on being the experts and being able to provide great quality service and products at the best prices anywhere.
In a highly competitive market we need to convey that despite government incentives and feed-in tariff rates being reduced by the government, solar has never been more affordable or economical for families. This is due to the significant fall in solar equipment prices, but this is set to change as international manufacturers start to go out of business. With electricity/utility prices set to rise even further, solar is a perfect option for domestic and commercial use.
I want a leaflet that is grabbing and compels people to ring me for a free, no obligation quotation and in-home energy assessment.
We want to differentiate ourselves from the stand-point of cutting out the middle man and being the local, trusted and expert installers.
We want to protect people from the projected 60% rise in electricity prices over the coming 8 years and allow them to produce their own electricity!

```html
<!DOCTYPE html>
<html lang="en">
<head>
<meta charset="utf-8">
<title>Harborlight Energy – Local Letter Drop</title>
<link rel="stylesheet" href="https://fonts.googleapis.com/css2?family=Arimo:wght@400;700&family=Roboto+Condensed:wght@700&family=Tinos:wght@400;700&display=swap">
<style>
:root{
  --stage:#1c1c1c;
  --blue:#1d4a9b;
  --blue-dark:#163b80;
  --yellow:#f6b51e;
  --white:#ffffff;
  --ink:#111111;
  --red:#d42a2a;
  --bar:#c9302c;
  --grid:#9a9a9a;
}
*{margin:0;padding:0;box-sizing:border-box}
html,body{width:1200px;height:900px;overflow:hidden;background:var(--stage)}
body{font-family:"Arimo",Arial,sans-serif}
.canvas{position:relative;width:1200px;height:900px;overflow:hidden;background:var(--stage)}
.side-label{position:absolute;top:22px;width:300px;text-align:center;color:var(--white);font:700 32px "Arimo",Arial,sans-serif;letter-spacing:.5px}
.side-label--front{left:163px}
.side-label--back{left:746px}

.flyer{position:absolute;top:70px;height:786px;background:var(--white);overflow:hidden}
.flyer--front{left:37px;width:555px}
.flyer--back{left:621px;width:550px}
.layer{position:absolute;left:0;top:0}

.photo{position:absolute}
.photo--couple{left:0;top:150px;width:555px;height:330px;background:linear-gradient(135deg,#ececec 0%,#d9d6d2 45%,#8d8a88 70%,#e8e6e3 100%)}
.photo--installer{left:0;top:0;width:550px;height:360px;background:linear-gradient(180deg,#8fb8e6 0%,#cfe0f2 30%,#2c4a8a 55%,#c7ccd3 100%)}

.front-headline{position:absolute;left:0;top:26px;width:555px;text-align:center;color:var(--white);font-weight:700;text-transform:uppercase}
.front-headline .lead{font-size:26px;line-height:31px}
.front-headline .sub{font-size:20px;line-height:26px}

.pitch{position:absolute;left:22px;top:507px;width:310px;font:700 25px/29px "Arimo",Arial,sans-serif;color:var(--ink)}
.brand{position:absolute;left:342px;top:522px;width:200px;display:flex;align-items:center;gap:10px}
.brand-dot{flex:none;width:24px;height:24px;border-radius:50%;background:var(--yellow)}
.brand-name{font:700 25px/27px "Arimo",Arial,sans-serif;color:var(--blue-dark)}
.front-body{position:absolute;left:22px;top:605px;width:512px;font-size:12.3px;line-height:18px;color:var(--ink)}
.front-call{position:absolute;left:0;top:727px;width:555px;text-align:center;color:var(--white);font:700 30px "Roboto Condensed",Arial,sans-serif;letter-spacing:.3px}
.front-call .num{font-size:34px}

.offer{position:absolute;left:0;top:372px;width:550px;text-align:center;color:var(--blue);font-weight:700;text-transform:uppercase}
.offer .big{font-size:18.5px;line-height:24px}
.offer .small{font-size:15px;line-height:20px}

.chart{position:absolute;left:30px;top:466px;width:250px}
.chart-title{font:700 12.5px "Arimo",Arial,sans-serif;color:var(--red);padding-left:23px}
.chart svg{display:block;margin-top:2px}

.pricing{position:absolute;left:288px;top:468px;width:240px}
.pricing-title{font:700 12.5px "Arimo",Arial,sans-serif;color:var(--blue);text-align:center;margin-bottom:20px}
.price-table{width:232px;margin-left:4px;border-collapse:collapse;table-layout:fixed;font-family:"Tinos","Times New Roman",serif;font-size:11px;color:var(--ink)}
.price-table th,.price-table td{border:1px solid #333;padding:2px 3px;height:29px}
.price-table th{font-weight:700;text-align:center;height:26px;line-height:11px}
.price-table td{text-align:center}
.price-table td.period{text-align:left;line-height:12px}
.col-kw{width:34px}.col-price{width:58px}.col-off{width:60px}.col-period{width:80px}
.pricing-note{font-size:7.6px;font-weight:700;color:var(--ink);margin-top:8px;margin-left:4px}

.savings{position:absolute;left:0;top:664px;width:550px;text-align:center;font:700 24px "Arimo",Arial,sans-serif;color:var(--red)}
.back-contact{position:absolute;left:0;top:710px;width:550px;text-align:center;color:var(--white);font-weight:700}
.back-contact .call{font-size:19px;line-height:26px}
.back-contact .call .num{font-size:26px}
.back-contact .line{font-size:16px;line-height:19px}
</style>
</head>
<body>
<main class="canvas">
  <div class="side-label side-label--front">FRONT</div>
  <div class="side-label side-label--back">BACK</div>

  <section class="flyer flyer--front">
    <div class="photo photo--couple" role="img" aria-label="Photo of a worried couple reading an electricity bill at a table"></div>
    <svg class="layer" width="555" height="786" viewBox="0 0 555 786" aria-hidden="true">
      <path d="M0 0H555V112C430 150 260 205 0 198Z" fill="var(--blue)"/>
      <path d="M0 198C260 205 430 150 555 112V128C430 170 260 220 0 212Z" fill="var(--yellow)"/>
      <path d="M0 212C260 220 430 170 555 128V140C430 182 260 228 0 222Z" fill="var(--white)"/>
      <path d="M0 420C160 470 360 470 555 438V786H0Z" fill="var(--white)"/>
      <path d="M0 420C160 470 360 470 555 438V452C360 482 160 482 0 440Z" fill="var(--yellow)"/>
      <path d="M0 705C180 660 380 668 555 700V786H0Z" fill="var(--yellow)"/>
      <path d="M0 715C180 676 380 684 555 712V786H0Z" fill="var(--blue)"/>
    </svg>
    <div class="front-headline">
      <div class="lead">Have you thought about solar?</div>
      <div class="sub">Are you paying too much for electricity?</div>
      <div class="sub">Would you like to reduce<br>or even eliminate your bills?</div>
    </div>
    <p class="pitch">........ then as your local solar installer, we can help you!</p>
    <div class="brand"><span class="brand-dot"></span><span class="brand-name">Harborlight<br>Energy</span></div>
    <p class="front-body">In thepast six years, electricity prices have gone up by more than 93% and are due to increase even further! Wehave helped thousands of households avoid electricity price hikes….and they have been incredibly happy with the savings. Now we would like to pass these savings on to you.</p>
    <div class="front-call">CALL US TODAY : <span class="num">1300 555 019</span></div>
  </section>

  <section class="flyer flyer--back">
    <div class="photo photo--installer" role="img" aria-label="Photo of an installer in a hi-vis vest fitting solar panels on a roof under a blue sky"></div>
    <svg class="layer" width="550" height="786" viewBox="0 0 550 786" aria-hidden="true">
      <path d="M0 330C180 320 380 322 550 360V786H0Z" fill="var(--yellow)"/>
      <path d="M0 342C180 334 380 338 550 378V786H0Z" fill="var(--white)"/>
      <rect x="0" y="696" width="550" height="6" fill="var(--yellow)"/>
      <rect x="0" y="702" width="550" height="84" fill="var(--blue)"/>
    </svg>
    <div class="offer">
      <div class="big">As your local installer we would like to<br>offer you a free, no obligation quote</div>
      <div class="small">and energy assessment<br>to see how solar can work for you</div>
    </div>

    <div class="chart">
      <div class="chart-title">Quarterly Electricity Bill Projections</div>
      <svg width="250" height="180" viewBox="0 0 250 180" font-family="Arimo, Arial, sans-serif" font-size="9" fill="var(--ink)">
        <g stroke="var(--grid)" stroke-width="1">
          <line x1="40" y1="5" x2="40" y2="140"/>
          <line x1="40" y1="140" x2="226" y2="140"/>
        </g>
        <g text-anchor="end">
          <text x="30" y="8">$1,400</text>
          <text x="30" y="27">$1,200</text>
          <text x="30" y="47">$1,000</text>
          <text x="30" y="66">$800</text>
          <text x="30" y="85">$600</text>
          <text x="30" y="104">$400</text>
          <text x="30" y="124">$200</text>
          <text x="30" y="143">$-</text>
        </g>
        <g fill="var(--bar)">
          <rect x="44" y="109.1" width="9" height="30.9"/>
          <rect x="62.5" y="100.5" width="9" height="39.5"/>
          <rect x="81" y="92.7" width="9" height="47.3"/>
          <rect x="99.5" y="84.6" width="9" height="55.4"/>
          <rect x="118" y="75.9" width="9" height="64.1"/>
          <rect x="136.5" y="68.6" width="9" height="71.4"/>
          <rect x="155" y="60" width="9" height="80"/>
          <rect x="173.5" y="51.8" width="9" height="88.2"/>
          <rect x="192" y="43.6" width="9" height="96.4"/>
          <rect x="210.5" y="27.2" width="9" height="112.8"/>
        </g>
        <g text-anchor="end" font-size="8.5">
          <text transform="translate(52 148) rotate(-45)">2004</text>
          <text transform="translate(70.5 148) rotate(-45)">2006</text>
          <text transform="translate(89 148) rotate(-45)">2008</text>
          <text transform="translate(107.5 148) rotate(-45)">2010</text>
          <text transform="translate(126 148) rotate(-45)">2012</text>
          <text transform="translate(144.5 148) rotate(-45)">2014</text>
          <text transform="translate(163 148) rotate(-45)">2016</text>
          <text transform="translate(181.5 148) rotate(-45)">2018</text>
          <text transform="translate(200 148) rotate(-45)">2020</text>
          <text transform="translate(218.5 148) rotate(-45)">2022</text>
        </g>
      </svg>
    </div>

    <div class="pricing">
      <div class="pricing-title">Special Knox Resident Prices</div>
      <table class="price-table">
        <colgroup><col class="col-kw"><col class="col-price"><col class="col-off"><col class="col-period"></colgroup>
        <thead>
          <tr><th>KW</th><th>PRICE</th><th>% off bill</th><th>Pay Back Period</th></tr>
        </thead>
        <tbody>
          <tr><td>1.5</td><td>$1650</td><td>35%</td><td class="period">2 years 10 months</td></tr>
          <tr><td>3</td><td>$4300</td><td>71%</td><td class="period">3 years 7 months</td></tr>
          <tr><td>5</td><td>$7000</td><td>100%</td><td class="period">4 years 2 months</td></tr>
        </tbody>
      </table>
      <p class="pricing-note">Figures based on average household energy usage of 17kws/day</p>
    </div>

    <p class="savings">Start enjoying your savings today!</p>
    <div class="back-contact">
      <div class="call">GIVE US A CALL TODAY ON <span class="num">1300 555 019</span></div>
      <div class="line">E-mail : hello@harborlightenergy.com</div>
      <div class="line">42 Lantern Grove, Boronia Vic 3155</div>
    </div>
  </section>
</main>
</body>
</html>
```